Managed Service Provider need new business cards

We are a small Maanged Service Provider of IT Services and need a new fresh design for our business cards. We want something impossible, fun and professional :)
Our services has a large range, but we are always fun and make sure our customers both get their issue sorted and also feel like they are "catching up with an old friend".
All our cards in the past has always been all black, with red and we need something fresher.
The back of card, we would like just a small list of what we do i think, but if someone has a better idea, please do something cool with the back of the card:
Managed IT Services
Productivity Solutions
Data Backup and Recovery
IT System Maintenance
Managed IT Security
More details can be found on our website qvtechworks.com.au
Industry/Entity Type
It Company
Contact Information for Business Card
Name: Simon Trelawny
Title: Director
Phone: 03 6158 4932
Mobile: 0417 582 139
Email: simon@qvtechworks.com.au
Web: www.qvtechworks.com.au
Look and feel
Each slider illustrates characteristics of the customer's brand and the style your logo design should communicate.

```html
<!DOCTYPE html>
<html lang="en">
<head>
<meta charset="utf-8">
<title>QV Techworks – Business Card</title>
<link href="https://fonts.googleapis.com/css2?family=Josefin+Sans:wght@400;600;700&display=swap" rel="stylesheet">
<style>
  :root {
    --stage: #1d1d1f;
    --card-white: #f4f4f4;
    --card-black: #0c0c0c;
    --brand-red: #e0252f;
    --ink-dark: #2a2a2a;
    --ink-light: #d8d8d8;
  }
  * { margin: 0; padding: 0; box-sizing: border-box; }
  html, body {
    width: 1200px; height: 900px; overflow: hidden;
    background: var(--stage);
    font-family: "Josefin Sans", sans-serif;
  }
  .stage {
    width: 1200px; height: 900px;
    display: flex; flex-direction: column; align-items: center; justify-content: center;
    gap: 48px;
  }
  .card {
    position: relative;
    width: 630px; height: 360px;
    border-radius: 30px;
    overflow: hidden;
    box-shadow: 0 18px 40px rgba(0,0,0,0.55);
  }
  /* Front */
  .card--front { background: var(--card-white); }
  .front-corner {
    position: absolute; left: 0; top: 0;
    width: 100%; height: 100%;
  }
  .brand {
    position: absolute;
    display: flex; align-items: center; gap: 12px;
    color: var(--brand-red);
    font-weight: 700;
    text-transform: uppercase;
    letter-spacing: 1px;
  }
  .brand__dot {
    width: 18px; height: 18px; border-radius: 50%;
    background: var(--brand-red);
  }
  .card--front .brand { right: 48px; top: 150px; font-size: 38px; }
  .identity { position: absolute; left: 48px; top: 200px; }
  .identity__name {
    color: var(--brand-red); font-weight: 700; font-size: 24px; letter-spacing: 0.5px;
  }
  .identity__title { color: var(--ink-dark); font-size: 16px; margin-top: 4px; }
  .contacts { list-style: none; margin-top: 16px; }
  .contacts li {
    display: flex; align-items: center; gap: 10px;
    color: var(--ink-dark); font-size: 15px; line-height: 1; margin-bottom: 7px;
  }
  .contacts svg { width: 16px; height: 16px; flex: none; }
  /* Back */
  .card--back { background: var(--card-black); }
  .card--back .brand {
    left: 0; right: 0; top: 88px; justify-content: center; font-size: 52px;
  }
  .services {
    position: absolute; left: 40px; right: 40px; bottom: 70px;
    text-align: center; color: var(--ink-light); font-size: 17px; line-height: 1.75;
  }
  .services .bullet { color: var(--brand-red); margin: 0 6px; }
</style>
</head>
<body>
<main class="stage">
  <section class="card card--front" aria-label="Business card front">
    <svg class="front-corner" viewBox="0 0 630 360" aria-hidden="true">
      <path d="M0 0 H330 C300 60 230 60 150 80 C80 98 30 120 0 170 Z" fill="var(--card-black)"/>
      <path d="M0 170 C30 120 80 98 150 80 C230 60 300 60 330 0" fill="none" stroke="var(--brand-red)" stroke-width="5"/>
    </svg>
    <div class="brand"><span class="brand__dot"></span>QV Techworks</div>
    <div class="identity">
      <p class="identity__name">Simon Trelawny</p>
      <p class="identity__title">Director</p>
      <ul class="contacts">
        <li>
          <svg viewBox="0 0 16 16" aria-hidden="true"><circle cx="8" cy="8" r="8" fill="var(--brand-red)"/><path d="M5 4.5 L6.8 4.2 L7.4 6.2 L6.4 7 Q7.2 8.8 9 9.6 L9.8 8.6 L11.8 9.2 L11.5 11 Q7 11.2 5 4.5Z" fill="#fff"/></svg>
          03 6158 4932
        </li>
        <li>
          <svg viewBox="0 0 16 16" aria-hidden="true"><circle cx="8" cy="8" r="8" fill="var(--brand-red)"/><rect x="5.5" y="3.5" width="5" height="9" rx="1" fill="#fff"/></svg>
          0417 582 139
        </li>
        <li>
          <svg viewBox="0 0 16 16" aria-hidden="true"><circle cx="8" cy="8" r="8" fill="var(--brand-red)"/><rect x="4" y="5" width="8" height="6" rx="0.8" fill="#fff"/><path d="M4 5.3 L8 8.4 L12 5.3" fill="none" stroke="var(--brand-red)" stroke-width="0.9"/></svg>
          simon@qvtechworks.com.au
        </li>
        <li>
          <svg viewBox="0 0 16 16" aria-hidden="true"><circle cx="8" cy="8" r="8" fill="var(--brand-red)"/><circle cx="8" cy="8" r="4" fill="none" stroke="#fff" stroke-width="1"/><path d="M4 8 H12 M8 4 Q5.5 8 8 12 Q10.5 8 8 4" fill="none" stroke="#fff" stroke-width="0.9"/></svg>
          www.qvtechworks.com.au
        </li>
      </ul>
    </div>
  </section>

  <section class="card card--back" aria-label="Business card back">
    <div class="brand"><span class="brand__dot"></span>QV Techworks</div>
    <p class="services">
      <span class="bullet">•</span>Managed IT Services <span class="bullet">•</span>Productivity Solutions <span class="bullet">•</span>Data Backup and Recovery<br>
      <span class="bullet">•</span>IT System Maintenance <span class="bullet">•</span>Managed IT Security
    </p>
  </section>
</main>
</body>
</html>
```